Pine Vale Accounting - New Postcard for B2B marketing

I need a postcard for my business that provides cloud-based bookkeeping services with LedgerCloud Online. Our clients are small independently owned businesses. Please use our website for inspiration (colors, content, etc)... www.PineValeAccounting.example.

Target Market(s)

Small, independently-owned businesses, including restaurants, retail stores, small medical practices, etc

Industry/Entity Type

Bookkeeper

Font styles to use
Serif

Colors
3276b5
155ea9
c4d6e9
85cae6
33a6d7

Requirements
Must have
• Must have my logo (see attached), business contact info (see website), description of services, blue color scheme
Nice to have
• Maybe add "Prices starting at $750/mo"
Content should match info on our website
4 x 6 horizontal postcard (see attached template)

```html
<!DOCTYPE html>
<html lang="en">
<head>
<meta charset="utf-8">
<title>Pine Vale Accounting – Postcard</title>
<link rel="stylesheet" href="https://fonts.googleapis.com/css2?family=Montserrat:wght@700;800;900&family=Merriweather:wght@400;700&family=Oswald:wght@500&display=swap">
<style>
  :root {
    --navy: #1b3c6e;
    --blue: #155ea9;
    --blue-mid: #3276b5;
    --cyan: #33a6d7;
    --cyan-light: #3ab6d6;
    --mist: #c4d6e9;
    --paper: #ffffff;
    --panel: #e9eaec;
    --ink: #1d1d1d;
    --stage: #5c5c5c;
  }
  * { margin: 0; padding: 0; box-sizing: border-box; }
  html, body { width: 894px; height: 1200px; overflow: hidden; background: var(--stage); }
  .canvas { position: relative; width: 894px; height: 1200px; }

  .postcard { position: absolute; left: 90px; width: 714px; height: 476px; background: var(--paper); overflow: hidden; }
  .postcard--front { top: 90px; }
  .postcard--back { top: 638px; }

  .shapes { position: absolute; inset: 0; }

  /* front */
  .hero-panel { position: absolute; left: 0; top: 0; width: 714px; height: 333px; background: var(--panel); }
  .hero-photo { position: absolute; left: 232px; top: 0; width: 482px; height: 333px;
    background: linear-gradient(100deg, var(--panel) 0%, #dfe6ec 18%, #b9c9d6 45%, #7f93a8 70%, #c9d3dc 100%); }
  .headline { position: absolute; left: 36px; top: 28px; font-family: "Montserrat", sans-serif; font-weight: 800;
    font-size: 42px; line-height: 38px; color: var(--navy); letter-spacing: 0.2px; }
  .headline .accent { color: var(--cyan-light); }
  .tagline { position: absolute; left: 45px; top: 123px; width: 200px; font-family: "Merriweather", serif; font-weight: 700;
    font-size: 16px; line-height: 21.6px; color: var(--blue); }
  .price { position: absolute; left: 46px; top: 260px; color: var(--paper); }
  .price__label { font-family: "Merriweather", serif; font-weight: 700; font-size: 14px; letter-spacing: 0.3px; }
  .price__amount { font-family: "Montserrat", sans-serif; font-weight: 800; font-size: 38px; line-height: 44px; color: var(--cyan-light); }
  .brand { position: absolute; display: flex; align-items: center; gap: 10px; font-family: "Merriweather", serif;
    font-weight: 400; color: var(--navy); white-space: nowrap; }
  .brand__mark { background: var(--blue-mid); flex: none; }
  .brand--front { left: 30px; top: 383px; font-size: 22px; }
  .brand--front .brand__mark { width: 22px; height: 22px; }
  .cta { position: absolute; left: 318px; top: 333px; width: 396px; height: 48px; line-height: 48px; text-align: center;
    font-family: "Oswald", sans-serif; font-weight: 500; font-size: 20px; color: var(--paper); white-space: nowrap; }
  .contact { position: absolute; left: 366px; top: 393px; display: flex; gap: 18px; align-items: flex-start; }
  .contact__icon { width: 46px; height: 50px; }
  .contact__phone { font-family: "Montserrat", sans-serif; font-weight: 700; font-size: 29px; line-height: 34px; color: var(--cyan-light); letter-spacing: 0.5px; white-space: nowrap; }
  .contact__line { font-family: "Merriweather", serif; font-size: 14px; line-height: 20px; color: var(--paper); margin-left: 4px; white-space: nowrap; }

  /* back */
  .services-title { position: absolute; left: 40px; top: 22px; font-family: "Montserrat", sans-serif; font-weight: 900;
    font-size: 21px; color: var(--paper); letter-spacing: 0.3px; }
  .service { position: absolute; left: 26px; display: flex; gap: 12px; }
  .service__icon { width: 38px; height: 38px; flex: none; margin-top: 4px; }
  .service__name { font-family: "Montserrat", sans-serif; font-weight: 800; font-size: 15px; color: var(--blue); line-height: 20px; white-space: nowrap; }
  .service__text { font-family: "Merriweather", serif; font-size: 11px; line-height: 14.8px; color: var(--ink); margin-top: 2px; }
  .service--books { top: 62px; }
  .service--books .service__text { width: 268px; }
  .service--reports { top: 205px; }
  .service--reports .service__text { width: 296px; }
  .service--payroll { top: 316px; }
  .service--payroll .service__text { width: 316px; }
  .promise { position: absolute; left: 35px; top: 412px; width: 390px; font-family: "Merriweather", serif; font-weight: 700;
    font-size: 14px; line-height: 18.5px; color: var(--paper); }
  .brand--back { left: 400px; top: 50px; font-size: 15px; }
  .brand--back .brand__mark { width: 15px; height: 15px; }
  .stamp-box { position: absolute; left: 620px; top: 22px; width: 74px; height: 85px; border: 1px solid #666; }
  .address-line { position: absolute; left: 442px; width: 230px; height: 1px; background: #333; }
  .address-line--1 { top: 205px; }
  .address-line--2 { top: 265px; }
  .address-line--3 { top: 327px; }
</style>
</head>
<body>
<div class="canvas">

  <section class="postcard postcard--front">
    <div class="hero-panel"></div>
    <div class="hero-photo" role="img" aria-label="Photo of a small team smiling and reviewing paperwork around a laptop in a bright office"></div>
    <svg class="shapes" width="714" height="476" viewBox="0 0 714 476" aria-hidden="true">
      <polygon points="0,253 268,253 298,333 0,333" fill="var(--navy)"/>
      <polygon points="298,333 714,333 714,381 316,381" fill="var(--cyan-light)"/>
      <polygon points="316,381 714,381 714,476 347,476" fill="var(--navy)"/>
    </svg>
    <h1 class="headline"><span class="accent">ACCOUNTING</span> FOR<br>YOUR BUSINESS</h1>
    <p class="tagline">Specializing in Cloud-Based Bookkeeping &amp; Payroll Processing with LedgerCloud Online by Northwind Software.</p>
    <div class="price">
      <div class="price__label">PRICES STARTING AT</div>
      <div class="price__amount">$750/mo</div>
    </div>
    <div class="brand brand--front"><span class="brand__mark"></span>Pine Vale Accounting</div>
    <div class="cta">BOOK A CALL TODAY FOR REQUEST QUOTE!</div>
    <div class="contact">
      <svg class="contact__icon" viewBox="0 0 46 50" aria-hidden="true">
        <rect x="9" y="2" width="26" height="46" rx="5" fill="var(--cyan-light)"/>
        <rect x="13" y="8" width="18" height="30" rx="1" fill="var(--navy)"/>
        <circle cx="22" cy="43" r="2" fill="var(--navy)"/>
        <path d="M2 26 q0 -8 7 -8 v20 q-7 0 -7 -8z" fill="var(--cyan-light)"/>
        <rect x="33" y="20" width="10" height="5" rx="2.5" fill="var(--cyan-light)"/>
        <rect x="33" y="27" width="10" height="5" rx="2.5" fill="var(--cyan-light)"/>
        <rect x="33" y="34" width="9" height="5" rx="2.5" fill="var(--cyan-light)"/>
      </svg>
      <div>
        <div class="contact__phone">1.877.555.0142</div>
        <div class="contact__line">info@pinevaleaccounting.example</div>
        <div class="contact__line">www.PineValeAccounting.example</div>
      </div>
    </div>
  </section>

  <section class="postcard postcard--back">
    <svg class="shapes" width="714" height="476" viewBox="0 0 714 476" aria-hidden="true">
      <polygon points="30,20 281,20 290,51 30,51" fill="var(--cyan-light)"/>
      <polygon points="0,402 416,402 446,476 0,476" fill="var(--navy)"/>
    </svg>
    <h2 class="services-title">OUR SERVICES</h2>

    <div class="service service--books">
      <svg class="service__icon" viewBox="0 0 38 38" aria-hidden="true">
        <ellipse cx="19" cy="30" rx="17" ry="6" fill="var(--cyan)"/>
        <ellipse cx="19" cy="22" rx="17" ry="6" fill="var(--cyan)" stroke="#fff" stroke-width="1.5"/>
        <ellipse cx="19" cy="12" rx="13" ry="10" fill="var(--cyan)" stroke="#fff" stroke-width="1.5"/>
        <text x="19" y="16" font-family="Montserrat, sans-serif" font-weight="800" font-size="11" fill="#fff" text-anchor="middle">$</text>
      </svg>
      <div>
        <h3 class="service__name">BOOKKEEPING</h3>
        <p class="service__text">Let us take over the day to day bookkeeping so you can get back to running your business. We offer LedgerCloud Online setup and ongoing bookkeeping, including daily journal entries, accounts payables &amp; receivables, bill pay, sales tax reporting &amp; payments, account reconciliation, and more.</p>
      </div>
    </div>

    <div class="service service--reports">
      <svg class="service__icon" viewBox="0 0 38 38" fill="none" stroke="var(--cyan)" stroke-width="1.5" aria-hidden="true">
        <path d="M8 3 h24 v32 h-20 l-4 -4z"/>
        <rect x="20" y="7" width="9" height="9"/>
        <path d="M11 12 h6 M11 20 h18 M11 24 h18 M11 28 h14"/>
        <rect x="2" y="18" width="3" height="10"/><rect x="5" y="14" width="3" height="14"/>
      </svg>
      <div>
        <h3 class="service__name">FINANCIAL REPORTING</h3>
        <p class="service__text">We'll provide easy to understand financial reports that allow you and your team to manage cash flow, create budgets and make forecasting decisions. Want real time data? Let us provide solutions with the latest in mobile apps and dashboards.</p>
      </div>
    </div>

    <div class="service service--payroll">
      <svg class="service__icon" viewBox="0 0 38 38" fill="none" stroke="var(--cyan)" stroke-width="1.5" aria-hidden="true">
        <circle cx="7" cy="7" r="4"/><circle cx="19" cy="5" r="4"/><circle cx="31" cy="7" r="4"/>
        <path d="M2 22 q0 -9 5 -9 q5 0 5 9 M14 20 q0 -10 5 -10 q5 0 5 10 M26 22 q0 -9 5 -9 q5 0 5 9"/>
        <path d="M6 24 h26 v6 h-26z M10 30 v6 M28 30 v6"/>
      </svg>
      <div>
        <h3 class="service__name">PAYROLL PROCESSING</h3>
        <p class="service__text">Whether you have 5 employees or 100+, payroll can be an overwhelming and time consuming task. We offer full service payroll processing, including employee on boarding and reporting.</p>
      </div>
    </div>

    <p class="promise">Our Certified LedgerCloud ProAdvisors have the Knowledge and Expertise to Ensure Professional, Accurate, High Quality Service.</p>

    <div class="brand brand--back"><span class="brand__mark"></span>Pine Vale Accounting</div>
    <div class="stamp-box"></div>
    <div class="address-line address-line--1"></div>
    <div class="address-line address-line--2"></div>
    <div class="address-line address-line--3"></div>
  </section>

</div>
</body>
</html>
```